Stationery for consulting company
Strategic Thinking. Inclusive Solutions. Measurable Impact
Project: Stationery for consulting company
Business Cards and Stationery
Professional
Benedo Ofurame Phd
Senior Partner
Plot 9 Umoru Close Oregun, Ikeja Lagos - Nigeria
Benedo.ofura@velmarq.com
www.velmarq.com
fdsfdffdsd

```html
<!DOCTYPE html>
<html lang="en">
<head>
<meta charset="utf-8">
<title>Velmarq Consulting — Business Card</title>
<link href="https://fonts.googleapis.com/css2?family=Roboto+Slab:wght@700&family=Montserrat:wght@400;700&display=swap" rel="stylesheet">
<style>
  :root {
    --bg: #d9dadc;
    --orange: #d45e2b;
    --green: #0f5a3a;
    --ink: #444;
    --muted: #888;
    --white: #ffffff;
    --rule: #cfcfcf;
  }
  * { margin: 0; padding: 0; box-sizing: border-box; }
  html, body { width: 1200px; height: 901px; overflow: hidden; }
  body { background: var(--bg); font-family: "Montserrat", sans-serif; position: relative; }

  .card {
    position: absolute; left: 300px; width: 600px; height: 345px;
    border-radius: 14px; overflow: hidden;
  }
  .card--front { top: 66px; background: var(--orange); display: flex; align-items: center; justify-content: center; gap: 18px; }
  .card--back { top: 484px; background: var(--white); }

  .front-mark { width: 46px; height: 46px; border-radius: 50%; background: var(--white); opacity: .9; }
  .front-name { font-weight: 700; font-size: 46px; letter-spacing: 3px; color: var(--white); }

  .brand { position: absolute; left: 20px; top: 22px; display: flex; align-items: center; gap: 10px; }
  .brand-mark { width: 30px; height: 30px; border-radius: 50%; background: var(--orange); }
  .brand-name { font-weight: 700; font-size: 19px; letter-spacing: 1.5px; color: var(--green); }

  .person { position: absolute; left: 20px; top: 175px; }
  .person-name { font-family: "Roboto Slab", serif; font-weight: 700; font-size: 30px; color: var(--green); }
  .person-role { font-size: 12px; color: var(--muted); margin-top: 2px; }

  .rule { position: absolute; left: 20px; right: 24px; top: 251px; height: 1px; background: var(--rule); }

  .contact { position: absolute; left: 20px; top: 270px; font-size: 12.5px; color: var(--ink); line-height: 19px; }
  .contact-row { display: flex; align-items: center; gap: 7px; }
  .contact-row svg { width: 10px; height: 10px; fill: var(--orange); }

  .address { position: absolute; right: 24px; top: 270px; font-size: 12.5px; color: var(--muted); line-height: 19px; text-align: right; }

  .foot-strip { position: absolute; left: 0; bottom: 0; width: 420px; height: 7px; background: var(--orange); }
  .foot-web {
    position: absolute; right: 0; bottom: 0; width: 212px; height: 30px;
    background: var(--green); clip-path: polygon(22px 0, 100% 0, 100% 100%, 0 100%);
    color: var(--white); font-size: 12px; display: flex; align-items: center; justify-content: flex-end; padding-right: 22px;
  }
</style>
</head>
<body>
  <section class="card card--front" aria-label="Card front">
    <span class="front-mark"></span>
    <span class="front-name">VELMARQ</span>
  </section>

  <section class="card card--back" aria-label="Card back">
    <div class="brand">
      <span class="brand-mark"></span>
      <span class="brand-name">VELMARQ CONSULTING</span>
    </div>

    <div class="person">
      <h1 class="person-name">Benedo Ofurame Phd</h1>
      <p class="person-role">Senior Partner</p>
    </div>

    <div class="rule"></div>

    <div class="contact">
      <div class="contact-row">
        <svg viewBox="0 0 10 10"><path d="M2 0.5 L4 2.8 L3 4 Q4.3 6 6 7 L7.2 6 L9.5 8 L8 9.6 Q4 9.6 0.4 2 Z"/></svg>
        <span>+234 (0) 809 417 6630</span>
      </div>
      <div class="contact-row">
        <svg viewBox="0 0 10 10"><rect x="0.5" y="2" width="9" height="6.5" rx="1"/></svg>
        <span>Benedo.ofura@velmarq.com</span>
      </div>
    </div>

    <div class="address">
      <p>Plot 9 Umoru Close Oregun</p>
      <p>Ikeja Lagos - Nigeria</p>
    </div>

    <div class="foot-strip"></div>
    <div class="foot-web">www.velmarq.com</div>
  </section>
</body>
</html>
```